Dorlin Commercial Truck / Trailer / RV Repair

Need a billboard design for our shop. Will include our logo below and want the word DORLIN on the top without the circle. Straighten out the letter "M" on the logo as well. Also will include a rough draft of a design and words I had in mind. All the words need to be included but the layout and design is up to you. Open to all options just needs to be easy to see and understand the message from the highway.

```html
<!DOCTYPE html>
<html lang="en">
<head>
<meta charset="utf-8">
<title>Dorlin Commercial Repair Shop – Billboard</title>
<link href="https://fonts.googleapis.com/css2?family=Montserrat:ital,wght@0,600;0,800;1,800&family=Oswald:wght@400;500&display=swap" rel="stylesheet">
<style>
  :root {
    --stage: #dfe3ea;
    --ink-dark: #1c1d20;
    --paper: #eef0f4;
    --brand-blue: #3d8fe0;
    --bar-blue: #5aaaf0;
    --white: #ffffff;
    --label: #2a2b2e;
    --rule: #9ea3ab;
  }
  html, body {
    margin: 0;
    width: 1200px;
    height: 900px;
    overflow: hidden;
    background: var(--stage);
  }
  .billboard {
    position: absolute;
    left: 40px;
    top: 255px;
    width: 1120px;
    height: 390px;
    background: var(--paper);
    outline: 8px solid var(--ink-dark);
    overflow: hidden;
    font-family: "Montserrat", sans-serif;
  }
  .billboard-shapes {
    position: absolute;
    inset: 0;
  }
  .brand-word {
    position: absolute;
    left: 96px;
    top: 18px;
    margin: 0;
    font-weight: 800;
    font-size: 46px;
    letter-spacing: 1px;
    color: var(--brand-blue);
  }
  .headline {
    position: absolute;
    left: 28px;
    top: 70px;
    margin: 0;
    font-weight: 800;
    font-size: 60px;
    line-height: 1;
    color: var(--white);
    letter-spacing: -1px;
  }
  .headline .accent { color: var(--brand-blue); }
  .subhead {
    position: absolute;
    left: 256px;
    top: 134px;
    margin: 0;
    font-weight: 800;
    font-style: italic;
    font-size: 28px;
    color: var(--brand-blue);
  }
  .headline-rule {
    position: absolute;
    left: 28px;
    top: 174px;
    width: 190px;
    height: 1px;
    background: var(--rule);
  }
  .services {
    position: absolute;
    left: 28px;
    top: 186px;
    display: flex;
    gap: 16px;
    margin: 0;
    padding: 0;
    list-style: none;
  }
  .service {
    width: 96px;
    text-align: center;
  }
  .service-photo {
    width: 96px;
    height: 96px;
    border-radius: 6px;
    border: 3px solid var(--white);
    box-sizing: border-box;
  }
  .service-photo.trucks { background: linear-gradient(160deg, #9bb3c6 0%, #b0623f 55%, #4a3a34 100%); }
  .service-photo.trailers { background: linear-gradient(160deg, #8a5a7a 0%, #d9a35a 50%, #7a5540 100%); }
  .service-photo.rv { background: linear-gradient(160deg, #5f6f78 0%, #b8bcbf 50%, #4f5a3e 100%); }
  .service-label {
    display: block;
    margin-top: 12px;
    font-weight: 600;
    font-size: 15px;
    color: var(--label);
  }
  .contact {
    position: absolute;
    left: 356px;
    top: 178px;
    display: flex;
    align-items: center;
    gap: 10px;
  }
  .contact-icon { width: 38px; height: 38px; }
  .phone {
    font-family: "Oswald", sans-serif;
    font-weight: 500;
    font-size: 44px;
    line-height: 1.1;
    color: var(--white);
    letter-spacing: -0.5px;
  }
  .quote-bar {
    position: absolute;
    left: 356px;
    top: 245px;
    width: 262px;
    height: 28px;
    margin: 0;
    background: var(--bar-blue);
    color: var(--white);
    font-family: "Oswald", sans-serif;
    font-size: 15px;
    line-height: 28px;
    padding-left: 14px;
    box-sizing: border-box;
    letter-spacing: 0.3px;
  }
  .amenities {
    position: absolute;
    left: 356px;
    top: 290px;
    margin: 0;
    font-family: "Oswald", sans-serif;
    font-weight: 400;
    font-size: 40px;
    line-height: 1.2;
    color: var(--label);
    letter-spacing: -0.5px;
  }
  .corner-mark {
    position: absolute;
    right: 26px;
    top: 26px;
    display: flex;
    align-items: center;
    gap: 10px;
  }
  .corner-mark-dot {
    width: 22px;
    height: 22px;
    border-radius: 50%;
    border: 3px solid #6b6e74;
    box-sizing: border-box;
  }
  .corner-mark-name {
    font-weight: 800;
    font-size: 28px;
    color: var(--brand-blue);
  }
</style>
</head>
<body>
  <section class="billboard" aria-label="Dorlin Commercial Repair Shop billboard">
    <svg class="billboard-shapes" viewBox="0 0 1120 390" width="1120" height="390">
      <defs>
        <linearGradient id="dark-panel" x1="0" y1="0" x2="1" y2="1">
          <stop offset="0" stop-color="#2c2d31"/>
          <stop offset="0.5" stop-color="#1f2023"/>
          <stop offset="1" stop-color="#2e3034"/>
        </linearGradient>
        <linearGradient id="truck-scene" x1="0" y1="0" x2="1" y2="1">
          <stop offset="0" stop-color="#c9c4b0"/>
          <stop offset="0.35" stop-color="#b53a30"/>
          <stop offset="0.65" stop-color="#8e2b24"/>
          <stop offset="0.85" stop-color="#e0a65a"/>
          <stop offset="1" stop-color="#4a4a48"/>
        </linearGradient>
      </defs>
      <polygon class="dark-panel" points="0,0 770,0 655,150 710,245 0,245" fill="url(#dark-panel)"/>
      <polygon class="truck-photo" role="img" aria-label="Photo of a red semi truck hauling a container trailer on a highway at sunset"
               points="815,0 1120,0 1120,280 780,280 700,150" fill="url(#truck-scene)"/>
    </svg>

    <p class="brand-word">DORLIN</p>
    <h1 class="headline">CO<span class="accent">MM</span>ERCIAL</h1>
    <p class="subhead">REPAIR SHOP</p>
    <div class="headline-rule"></div>

    <ul class="services">
      <li class="service">
        <div class="service-photo trucks" role="img" aria-label="Photo of a red semi truck"></div>
        <span class="service-label">TRUCKS</span>
      </li>
      <li class="service">
        <div class="service-photo trailers" role="img" aria-label="Photo of a truck with trailer on a desert road"></div>
        <span class="service-label">TRAILERS</span>
      </li>
      <li class="service">
        <div class="service-photo rv" role="img" aria-label="Photo of a silver RV camper in the mountains"></div>
        <span class="service-label">RV</span>
      </li>
    </ul>

    <div class="contact">
      <svg class="contact-icon" viewBox="0 0 40 40" aria-hidden="true">
        <circle cx="20" cy="20" r="17" fill="none" stroke="#3d8fe0" stroke-width="2.5"/>
        <path d="M13 11c1.5-1 3-1 3.5 0l2 4c.4 1-.3 1.6-1.2 2.2.8 2 2.4 3.6 4.5 4.5.6-.9 1.2-1.6 2.2-1.2l4 2c1 .5 1 2 0 3.5-1.5 2-4 2.5-7 1-4-2-7-5-9-9-1.5-3-1-5.5 1-7z" fill="#3d8fe0"/>
      </svg>
      <span class="phone">888.555.0142</span>
    </div>
    <p class="quote-bar">CALL OR COME BY FOR A QUOTE!</p>
    <p class="amenities">PARKING &amp; STORAGE AVAILABLE</p>

    <div class="corner-mark">
      <span class="corner-mark-name">DORLIN</span>
      <span class="corner-mark-dot"></span>
    </div>
  </section>
</body>
</html>
```